Inspiring Wordpress Design for Brightpath Figure Renewal: Assured Contest

We need a web design for a medical weight loss clinic near San Francisco. We would like for our site to be similar to http://www.trimlarkhaven.com:

The winning design will communicate a youthful, energetic, and fun vibe. We want to imply success and vitality in contrast to the guilt, shame, and burden of traditional weight loss. At the same time, it is a very scientifically oriented and physician supervised so we need it to convey authority and science at the same time.

Our logo and font files are attached.

Target Demographic: 30-50 year old women of White, Asian, Latin, and African American Backgrounds. Income $35-120k.

Target Market(s)

We are a medical Weight Loss Center. Our target audience is women aged 30-55 in low middle to middle class, incomes from $30k to $150k per year. Target Audience is of mixed race including white, Latin, African American and Asian.

Industry/Entity Type

Clinic

Font styles to use
Other font styles liked:
• 738162 Acrom Family (OTF) $160.00 The Velvet Quarry Ltd package Desktop users: 10 - 915374 Twentieth Century 1 Volume (OTF) $157.00 Glyphorra package Desktop users: 5 - 608293 Twentieth Century 2 Volume (Win TTF) $105.00 Glyphorra package

Requirements
Must have
• Tabs:
Science of Weight Loss Success
Success Stories
Location and Hours
Contact Us
Espanol

Need an Area for Our Slogan ( exact slogan TBD)

Please include Stock Images and links to those images in your design.

We would Like to Include Three Buttons in the design:
1. Stop the Low Calorie Starvation Diet
2. Why Coral Bayslim
3. Become a Skinny Fat Burner Today
Nice to have
• Fonts that we have purchased are attached. Please use these.

```html
<!DOCTYPE html>
<html lang="en">
<head>
<meta charset="utf-8">
<title>Coral Bayslim – Medical Weight Loss Centers</title>
<link href="https://fonts.googleapis.com/css2?family=Quicksand:wght@500;600&family=Questrial&family=Roboto:ital,wght@0,400;0,500;0,700;1,400&display=swap" rel="stylesheet">
<style>
:root{
  --teal:#24bcb0;
  --teal-dark:#16584f;
  --teal-deep:#1b6b62;
  --teal-deeper:#135a52;
  --orange:#f6ab00;
  --ink:#444;
  --page:#f1f1f1;
  --slide-blue:#4a84a6;
}
*{box-sizing:border-box;margin:0;padding:0}
html,body{width:854px;height:1200px;overflow:hidden}
body{position:relative;background:#fff;font-family:"Roboto",sans-serif;color:var(--ink)}
.abs{position:absolute}
.top-band{left:0;top:0;width:854px;height:405px;background:var(--page);border-top:3px solid #e9e3a6}
.brand{left:95px;top:20px}
.brand-name{font-family:"Quicksand",sans-serif;font-weight:600;font-size:30px;line-height:32px;color:var(--orange);display:flex;align-items:center;gap:8px}
.brand-dot{width:13px;height:13px;border-radius:50%;background:var(--teal)}
.brand-tag{font-family:"Questrial",sans-serif;font-size:10.5px;letter-spacing:2.4px;color:var(--teal-dark);margin-top:4px}
.top-phone{left:498px;top:29px;font-family:"Questrial",sans-serif;font-size:23px;color:var(--orange);display:flex;align-items:center;gap:4px}
.social-dot{top:32px;width:21px;height:21px;border-radius:50%;background:#9fbfbb}
.nav{left:94px;top:80px;width:667px;height:39px;background:linear-gradient(#33cdbf,#1eb0a3);border-radius:2px;display:flex;align-items:center;padding:0 10px;font-family:"Questrial",sans-serif;font-size:12.5px;color:#fff;white-space:nowrap;justify-content:space-between}
.nav .sep{font-size:6px}
.nav .current{color:var(--teal-dark)}
.nav .lang{border:1px solid #9ae6df;background:#2ec2b5;padding:2px 7px}
.slider{left:93px;top:132px;width:668px;height:262px;background:#fff;border:1px solid #ddd}
.slide{left:100px;top:139px;width:654px;height:247px;background:linear-gradient(90deg,#e9f1f6 0%,#bcd3e2 35%,#6c9bb8 60%,var(--slide-blue) 70%)}
.hex-label{font-family:"Questrial",sans-serif;font-size:10px;color:#fff;white-space:nowrap}
.slogan{left:495px;top:236px;font-family:"Questrial",sans-serif;font-size:21px;line-height:27px;color:#fff;letter-spacing:.5px;white-space:nowrap}
.cta{left:494px;top:303px;width:144px;height:33px;background:var(--orange);color:#fff;font-family:"Questrial",sans-serif;font-size:16px;display:flex;align-items:center;justify-content:center}
.pager{left:668px;top:357px;width:86px;height:29px;background:rgba(255,255,255,.85);display:flex;align-items:center;justify-content:center;gap:5px}
.pager i{width:9px;height:9px;border-radius:50%;border:1px solid var(--teal)}
.pager i.on{background:var(--teal)}
.feature{top:446px;width:205px;height:94px;background:#fff;border:1px solid #ddd;text-align:center;font-family:"Questrial",sans-serif;font-size:16px;line-height:18px;letter-spacing:1px;color:var(--teal-dark);padding-top:26px}
.feature-dot{top:434px;width:24px;height:24px;border-radius:50%;background:var(--orange)}
.feature-shadow{top:538px;width:205px;height:14px;background:radial-gradient(ellipse at top,rgba(0,0,0,.28),rgba(0,0,0,0) 70%)}
.heading{font-family:"Quicksand",sans-serif;font-weight:600;color:var(--teal-dark);white-space:nowrap}
.heading em{font-style:normal;color:var(--orange)}
.rule{height:1px;background:#ddd}
.body-copy{font-size:8.8px;line-height:14.2px;color:var(--ink)}
.btn{color:#fff;font-size:9px;font-weight:700;display:flex;align-items:center;justify-content:center;white-space:nowrap}
.about{left:94px;top:736px;width:667px;height:148px;background:linear-gradient(90deg,#e5e6eb,#eeeff2 70%,#f7f7f8)}
.photo{background:linear-gradient(#dfe6ee,#c7d3e2)}
.story-card{top:942px;width:87px;height:75px;background:#fff;border:1px solid #ddd;text-align:center;font-size:9px;color:#555}
.story-card .photo{margin:4px auto 0;width:79px;height:50px}
.quote{top:942px;width:222px;font-size:8.3px;line-height:14px;font-style:italic;color:#555}
.quote b{color:#ccc;font-size:18px;line-height:10px;font-style:normal;margin-right:4px}
.footer{left:0;top:1044px;width:854px;height:126px;background:var(--teal-deep);color:#fff}
.footer h4{font-family:"Questrial",sans-serif;font-weight:400;font-size:14px;position:absolute;top:10px;white-space:nowrap}
.footer .frule{position:absolute;top:30px;height:1px;background:#3f8a81}
.links{left:94px;top:37px;list-style:none;font-size:9px;line-height:16.6px;white-space:nowrap}
.links li::before{content:"› ";color:#8cc}
.hours{left:274px;top:39px;width:168px;height:73px;background:#0f5048;font-size:9px;padding:12px 10px}
.hours div{display:flex;justify-content:space-between;margin-bottom:8px}
.contact{font-size:9px}
.follow{font-size:9px;display:flex;align-items:center;gap:8px;white-space:nowrap}
.follow i{width:20px;height:20px;border-radius:50%;background:#0f4a43}
.copyright{left:0;top:1170px;width:854px;height:30px;background:var(--teal-deeper);color:#dfeeec;font-size:9px;display:flex;align-items:center;justify-content:center}
</style>
</head>
<body>
<div class="abs top-band"></div>

<header>
  <div class="abs brand">
    <div class="brand-name"><span>Coral Bayslim</span><span class="brand-dot"></span></div>
    <div class="brand-tag">MEDICAL WEIGHT LOSS CENTERS</div>
  </div>
  <div class="abs top-phone">
    <svg width="18" height="18" viewBox="0 0 24 24"><path fill="#f6ab00" d="M6.6 10.8a15 15 0 0 0 6.6 6.6l2.2-2.2c.3-.3.7-.4 1-.2 1.1.4 2.3.6 3.6.6.6 0 1 .4 1 1V20c0 .6-.4 1-1 1A17 17 0 0 1 3 4c0-.6.4-1 1-1h3.5c.6 0 1 .4 1 1 0 1.3.2 2.5.6 3.6.1.3 0 .7-.2 1z"/></svg>
    415-555-0187
  </div>
  <span class="abs social-dot" style="left:688px"></span>
  <span class="abs social-dot" style="left:714px"></span>
  <span class="abs social-dot" style="left:740px"></span>
  <nav class="abs nav">
    <span class="current">Home</span><span class="sep">●</span>
    <span>Science of Weight Loss Success</span><span class="sep">●</span>
    <span>Success Stories</span><span class="sep">●</span>
    <span>Location and Hours</span><span class="sep">●</span>
    <span>Contact Us</span><span class="sep">●</span>
    <span class="lang">Espanol</span>
  </nav>
</header>

<section>
  <div class="abs slider"></div>
  <div class="abs slide" role="img" aria-label="Smiling woman touching a hexagon interface of weight loss benefits"></div>
  <span class="abs hex-label" style="left:208px;top:144px">Physician Supervised</span>
  <span class="abs hex-label" style="left:321px;top:158px">Youthful</span>
  <span class="abs hex-label" style="left:411px;top:158px">Energetic</span>
  <span class="abs hex-label" style="left:222px;top:184px">Healthy Hormones</span>
  <span class="abs hex-label" style="left:464px;top:183px">Habit Transformation</span>
  <span class="abs hex-label" style="left:419px;top:209px">Faster Metabolism</span>
  <span class="abs hex-label" style="left:251px;top:234px">Personalized</span>
  <span class="abs hex-label" style="left:380px;top:248px">Vitamin Therapies</span>
  <div class="abs slogan">"Innovative Weight<br>Loss Solutions for All"</div>
  <div class="abs cta">Get Started Now</div>
  <div class="abs pager"><i class="on"></i><i></i><i></i><i></i><i></i></div>
</section>

<section>
  <div class="abs feature" style="left:94px">STOP<br>YO-YO<br>DIETING</div>
  <div class="abs feature" style="left:324px">BECOME A<br>SKINNY<br>FAT BURNER</div>
  <div class="abs feature" style="left:555px">GET<br>STARTED<br>TODAY</div>
  <span class="abs feature-dot" style="left:185px"></span>
  <span class="abs feature-dot" style="left:415px"></span>
  <span class="abs feature-dot" style="left:646px"></span>
  <span class="abs feature-shadow" style="left:94px"></span>
  <span class="abs feature-shadow" style="left:324px"></span>
  <span class="abs feature-shadow" style="left:555px"></span>
</section>

<section>
  <h2 class="abs heading" style="left:94px;top:562px;font-size:23px">Welcome to <em>Coral Bayslim</em></h2>
  <div class="abs rule" style="left:94px;top:598px;width:667px"></div>
  <p class="abs body-copy" style="left:94px;top:607px;width:667px">Lorem ipsum dolor sit amet, consectetuer adipiscing elit, sed diam nonummy nibh euismod tincidu ut laoreet dolore magna aliquam erat volutpat. Ut wisi enim ad minim veniam, quis nostrud exerci tation ullamcorper suscipit lobortis nisl ut aliquip ex ea commodo consequat. Duis autem vel eum iriur dolor in hendrerit in vulputate velit esse molestie consequat, vel illum dolore eu feugiat nulla facilisis at vero eros et accumsan et iusto odio dignissim qui blandit praesent luptatum zzril minim veniam, quis nostrud exerci tation ullamcorper suscipit lobortis nisl ut aliquip ex ea commodo consequat. Duis autem vel eum iriur dolor in hendrerit in vulputate velit esse molestie consequat, vel illum dolore eu feugiat nulla facilisis at vero eros et accumsan et iusto odio dignissim qui blandit praesent luptatum zzril delenit augue dui dolore te feugait nulla facilisi.</p>
  <div class="abs btn" style="left:94px;top:699px;width:59px;height:20px;background:var(--teal)">Know More</div>
</section>

<section>
  <div class="abs about"></div>
  <div class="abs photo" style="left:640px;top:736px;width:121px;height:148px;background:linear-gradient(90deg,rgba(220,228,238,0),#c9d6e6)" role="img" aria-label="Smiling clinic founder holding a tablet"></div>
  <h2 class="abs heading" style="left:108px;top:748px;font-size:23px">About the <em>Founders</em></h2>
  <p class="abs body-copy" style="left:108px;top:782px;width:535px;font-size:8.8px;line-height:14.8px;font-weight:700;color:#333">Lorem ipsum dolor sit amet, consectetuer adipiscing elit, sed diam nonummy Lorem ipsum dolor sit amet, consectetuer adipiscing elit, sed diam nonummyLorem ipsum dolor sit amet, consectetuer adipiscing elit, sed diam nonummyLorem ipsum dolor sit amet, consectetuer adipiscing elit, sed diam nonummyLorem ipsum dolor sit amet, consectetuer adipiscing elit, sed diam nonummyLorem ipsum dolor sit amet, consectetuer adipiscing elit, sed diam nonummy</p>
  <div class="abs btn" style="left:107px;top:854px;width:60px;height:17px;background:var(--orange);color:#333">Know More</div>
</section>

<section>
  <h2 class="abs heading" style="left:94px;top:901px;font-size:19px">Success <em>Stories</em></h2>
  <div class="abs rule" style="left:94px;top:930px;width:667px"></div>
  <div class="abs story-card" style="left:93px"><div class="photo" role="img" aria-label="Portrait of a happy client"></div><div style="margin-top:4px">Miss Arden</div></div>
  <p class="abs quote" style="left:193px"><b>“</b>Lorem ipsum dolor sit amet conseceuer adipisci sed diam nonummy nibh euismod tincidunt ut laoreet d magna quam erat volutpat. Ut wisi enim ad minim veiam, nostrud exerci tation ullamcorper susciplobortis nisl u ullamcorper suscipi.</p>
  <div class="abs story-card" style="left:440px"><div class="photo" role="img" aria-label="Client giving a thumbs up"></div><div style="margin-top:4px">Miss Arden</div></div>
  <p class="abs quote" style="left:541px"><b>“</b>Lorem ipsum dolor sit amet conseceuer adipisci sed diam nonummy nibh euismod tincidunt ut laoreet d magna quam erat volutpat. Ut wisi enim ad minim veiam, nostrud exerci tation ullamcorper susciplobortis nisl u ullamcorper suscipi.</p>
</section>

<footer class="abs footer">
  <h4 style="left:94px">Quick Links</h4><div class="frule" style="left:94px;width:158px"></div>
  <ul class="abs links">
    <li>Home</li><li>Science of Weight Loss Success</li><li>Success Stories</li><li>Location and Hours</li><li>Contact Us</li>
  </ul>
  <h4 style="left:274px">Opening Hours</h4><div class="frule" style="left:274px;width:168px"></div>
  <div class="abs hours">
    <div><span>▦ Monday to<br>&nbsp;&nbsp;&nbsp;Saturday</span><span>8:00 AM - 4:00 PM</span></div>
    <div><span>▦ Sunday</span><span>Closed</span></div>
  </div>
  <h4 style="left:470px">Contact Us</h4><div class="frule" style="left:470px;width:160px"></div>
  <div class="abs contact" style="left:470px;top:40px;display:flex;gap:8px">
    <svg width="12" height="16" viewBox="0 0 12 16"><path fill="#fff" d="M6 0a6 6 0 0 0-6 6c0 4.5 6 10 6 10s6-5.5 6-10a6 6 0 0 0-6-6zm0 8.5A2.5 2.5 0 1 1 6 3.5a2.5 2.5 0 0 1 0 5z"/></svg>
    <div><b>Standard dummy</b><br>Lorem Ipsum is simply dummy</div>
  </div>
  <div class="abs contact" style="left:470px;top:77px;display:flex;gap:8px;align-items:center;font-size:12px">
    <svg width="12" height="12" viewBox="0 0 24 24"><path fill="#fff" d="M6.6 10.8a15 15 0 0 0 6.6 6.6l2.2-2.2c.3-.3.7-.4 1-.2 1.1.4 2.3.6 3.6.6.6 0 1 .4 1 1V20c0 .6-.4 1-1 1A17 17 0 0 1 3 4c0-.6.4-1 1-1h3.5c.6 0 1 .4 1 1 0 1.3.2 2.5.6 3.6.1.3 0 .7-.2 1z"/></svg>415-555-0187
  </div>
  <div class="abs contact" style="left:470px;top:101px;display:flex;gap:8px;align-items:center">
    <svg width="12" height="9" viewBox="0 0 12 9"><rect width="12" height="9" fill="#fff"/><path d="M0 0l6 5 6-5" stroke="#1b6b62" fill="none"/></svg>info@coralbayslim.com
  </div>
  <h4 style="left:656px">Stay in Touch</h4><div class="frule" style="left:656px;width:105px"></div>
  <div class="abs follow" style="left:656px;top:40px"><i></i>CHATTERBOOK</div>
  <div class="abs follow" style="left:656px;top:66px"><i></i>REVIEWLY</div>
  <div class="abs follow" style="left:656px;top:92px"><i></i>MAPSPHERE PLACE</div>
</footer>
<div class="abs copyright">© 2014 .Coralbayslim.All Rights Reserved.</div>
</body>
</html>
```